【業務の内容】
建物(鉄筋(鉄骨)コンクリート躯体)の寿命が、あとどれくらい
残っているのか(=寿命)を評価する業務

【なぜこの業務が必要か】
・いまお住まいのマンションの将来計画を考えるために重要な基礎資料
例えば
・「建物寿命は、あと50年以上あるので、しっかりと設備も改修しよう」
・「建物寿命は、あと50年以上あるので、耐震補強を考えよう」
・「建物寿命が20年程度しか残っていないから、延命のための改修をしよう」
・「建物寿命が20年程度しか残っていないから、建替えの検討をしよう」
・残存寿命が長いなら、耐震補強や給排水設備の改修、共用部のリニューアル等を
実施する価値がある、と判断できる

【この業務を推す背景】
・築30年、40年を超える高経年マンションが増えてきている
・首都圏では大地震の確率が30年以内に70%と言われており。1981年以前の旧耐震
基準の建物は、すでに築40年を超えており、耐震補強工事を行うか、建替えるかの
選択を迫られている

【業務の費用(目安・税別)】 ※あくまでも目安
・1棟当たり 基本料金300,000+コア抜き50,000/ヶ所(1フロアあたり1ヶ所)

例)5階建て1棟のマンションの場合
基本料金300,000+(50,000×5ヶ所)=550,000(税別)
【訴求したい事】
・建物の寿命評価に特化しているので、耐震診断等と比べて比較的
安価に実施できる
・短期間で結果が分かる(着手後およそ1か月程度)
・これからマンションにどれだけ維持修繕や改良などの投資するかという
検討をする際の客観的裏付けのある基礎資料になる
・耐用年数は「集合住宅躯体の長期保全評価指針・同付録」(日本建築
学会)の示す算定式を使って算出する

【特に注意・留意すべき事象】
・「寿命が長い」=「安全」ではない
建物耐用年数が長くても、現在の耐震性能基準に達していなければ大地震で
大破・倒壊の危険性がある。躯体寿命と建物の安全性は全く別物
・建物の寿命と設備(給排水管や電気設備など)の寿命は別物
株式会社環創プラン 本社
〒150-0074
東京都渋谷区桜見台7-13-6朝陽ビル
TEL:03-6928-4171(代)
FAX:03-6928-4178

西日本支社
大阪事務所
〒530-0086
大阪府大阪市北区松風町 6-3-18 青葉セントラルビル
TEL:06-6384-2051
FAX:06-6384-2052

西日本支社
広島事務所
〒730-0094
広島県広島市中区千草通3-8-12浜辺ビル5F
TEL:082-517-6820
FAX:082-517-6829
A4
両面
赤系、緑系、水色系
• 高解像度JPG (.jpg)
• イラストレーター形式 (.ai)
使用可能な画像、図(こちらもチラシ作成上に入れてほしいがわかりやすくいじってもらってOKです)、会社ロゴ等全て添付します。

業界関係者ではなく、一般のかた(いわゆる「素人」)が、パッとみてどう感じるだろうか、という
目線で選定しました。
・あまり小難しい印象は与えず、明快なデザイン
・「マンション販売のチラシ」や「水道修理業者」と勘違いされない
というようなところで差がありました。

はじめてこのワークバザールを利用したのですが、このように色々なご提案をいただき、
正直、驚き(もちろん嬉しい方です)でした。
やはりプロにお任せするだけのことがあると痛感し、
我々の業務も同じような驚きをお客様にお届けできるように心がけたいと思います。

この度はご提案いただきまして、誠にありがとうございました。

```html
<!DOCTYPE html>
<html lang="ja">
<head>
<meta charset="utf-8">
<title>耐久性調査 サービスのご案内</title>
<link rel="stylesheet" href="https://fonts.googleapis.com/css2?family=Noto+Sans+JP:wght@400;500;700;900&display=swap">
<style>
:root{
  --navy:#1d3767;
  --blue:#2b74c4;
  --sky:#5aa7de;
  --pale:#e3eff9;
  --paper:#ffffff;
  --ink:#2a2f3a;
  --grey:#6b7380;
}
*{margin:0;padding:0;box-sizing:border-box}
html,body{width:846px;height:1200px;overflow:hidden;background:var(--paper)}
body{font-family:"Noto Sans JP",sans-serif;color:var(--ink);position:relative}
.flyer{position:relative;width:846px;height:1200px;overflow:hidden;background:var(--paper)}
.building-photo{position:absolute;left:300px;top:0;width:546px;height:380px;
  background:linear-gradient(120deg,#bcd2e6 0%,#e6eef6 45%,#ffffff 90%)}
.topline{position:absolute;left:20px;top:16px;font-size:30px;font-weight:900;color:var(--navy);letter-spacing:1px;background:var(--paper);padding:2px 10px}
.title-block{position:absolute;right:60px;top:125px;text-align:right;color:var(--navy)}
.title-block .kicker{font-size:20px;font-weight:700;color:var(--navy);margin-right:20px}
.title-block h1{font-size:98px;font-weight:900;color:var(--blue);letter-spacing:2px;line-height:1.15;margin-top:8px}
.title-block .sub{font-size:36px;font-weight:700;color:var(--navy);margin-top:2px}
.core-photo{position:absolute;left:0;top:380px;width:846px;height:560px;
  background:linear-gradient(90deg,#f4f8fc 0%,#e8f0f8 45%,#c9d4df 75%,#aab6c2 100%)}
.lead{position:absolute;left:60px;top:405px;width:640px}
.lead h2{font-size:29px;font-weight:900;color:var(--blue);line-height:1.45;white-space:nowrap}
.lead p{margin-top:16px;font-size:17px;font-weight:700;line-height:1.75;color:var(--ink)}
.why{position:absolute;left:56px;top:690px;width:400px;background:rgba(255,255,255,.92);border:2px solid var(--blue)}
.why h3{background:var(--navy);color:#fff;font-size:18px;font-weight:700;text-align:center;padding:7px 0}
.why p{padding:14px 16px 16px;font-size:12.5px;line-height:1.85;color:var(--ink)}
.merit{position:absolute;top:735px;width:160px;height:160px;border-radius:50%;background:rgba(43,116,196,.9);color:#fff;display:flex;align-items:center;justify-content:center;text-align:center;font-size:17px;font-weight:700;line-height:1.5}
.merit.a{left:480px}
.merit.b{left:648px}
.contact{position:absolute;left:56px;top:950px;width:500px}
.contact .note{font-size:12px;color:var(--grey)}
.contact .company{display:flex;align-items:baseline;gap:20px;margin-top:4px}
.contact .company strong{font-size:24px;font-weight:900;color:var(--navy)}
.contact .company span{font-size:13px;color:var(--grey)}
.office{display:flex;gap:12px;margin-top:7px;font-size:11.5px;line-height:1.45}
.office .label{width:78px;flex:none;background:var(--navy);color:#fff;font-size:11px;text-align:center;padding:3px 2px;align-self:flex-start;line-height:1.4}
.group{position:absolute;right:56px;top:990px;display:flex;align-items:center;gap:14px}
.group .mark{width:44px;height:44px;background:var(--blue)}
.group strong{font-size:28px;font-weight:700;color:var(--navy)}
.group-note{position:absolute;right:56px;top:1085px;width:270px;font-size:11px;line-height:1.6;color:var(--grey)}
</style>
</head>
<body>
<div class="flyer">
  <div class="building-photo" role="img" aria-label="マンション外観の写真（淡い青色調）"></div>
  <div class="topline">マンション［ 鉄筋（鉄骨）/ コンクリート躯体 ］</div>

  <div class="title-block">
    <div class="kicker">マンションの長寿命化コンサルタント</div>
    <h1>耐久性調査</h1>
    <div class="sub">サービスのご案内</div>
  </div>

  <div class="core-photo" role="img" aria-label="コンクリートコアのサンプルを手に持つ写真"></div>

  <div class="lead">
    <h2>各階のコンクリートコア抜き調査により<br>建物の寿命を調査・評価いたします。</h2>
    <p>建物の寿命推定を行い、<br>構造躯体の残りの対応年数を把握することで<br>それに即した修繕計画を策定し、<br>長期的な改修計画の合理化を図ります。</p>
  </div>

  <section class="why">
    <h3>なぜ今調査が必要なのか？</h3>
    <p>現在日本では、マンションストックが年々増えており、築30～40年を超える高経年マンションが増加傾向にあります。首都圏の大地震の発生確率も高まる中、旧耐震基準の建物は耐震補強か建替えかの選択を迫られています。残存寿命を把握し、将来計画の基礎資料とすることが「耐久性調査」の目的です。設備や改修への投資を判断する客観的な裏付けとなります。</p>
  </section>

  <div class="merit a">短期間・低コストで<br>調査が可能</div>
  <div class="merit b">建物の現状と<br>対応年数の把握<br>が可能</div>

  <section class="contact">
    <div class="note">ご相談・ご質問等ございましたら、お気軽にお問い合わせください。</div>
    <div class="company"><strong>株式会社環創プラン</strong><span>https://www.kanso-plan.co.jp</span></div>
    <div class="office"><div class="label">本社</div>
      <div>〒150-0074<br>東京都渋谷区桜見台7-13-6朝陽ビル<br>TEL:03-6928-4171（代） FAX:03-6928-4178</div></div>
    <div class="office"><div class="label">西日本支社<br>大阪事務所</div>
      <div>〒530-0086<br>大阪府大阪市北区松風町 6-3-18 青葉セントラルビル<br>TEL:06-6384-2051 FAX:06-6384-2052</div></div>
    <div class="office"><div class="label">西日本支社<br>広島事務所</div>
      <div>〒730-0094<br>広島県広島市中区千草通3-8-12浜辺ビル5F<br>TEL:082-517-6820 FAX:082-517-6829</div></div>
  </section>

  <div class="group"><div class="mark"></div><strong>環創プラングループ</strong></div>
  <p class="group-note">マンション管理組合様との対話を重ねて多数の調査実績があり、お住まいの建物の将来計画をお手伝いします。</p>
</div>
</body>
</html>
```